The Pipe Lantern business cards

Hi
i have attached a photo, this is how i want the front of my business card to look like:
i want the water drop on the right to be orange
and the water drop on the left to be gloss black
"The" and "Pty Ltd." will be in the same orange as the water drop
and "Pipe Lantern" will be in white
The background of the logo will be a matte black
on the back of the business card i need the following info:
'The Pipe Lantern pty ltd. '
'Plumbing . Drainage . Gas Fitting . Roofing . Jet Blasting . CCTV . '
Also my contact details:
Cal Yardley
0418672913
thepipelantern@mailkestrel.com
Licence# 583016K
Target Market(s)
Strata managers, building managers, the general public
Industry/Entity Type
Business

```html
<!DOCTYPE html>
<html lang="en">
<head>
<meta charset="utf-8">
<title>The Pipe Lantern – Business Card Back</title>
<link rel="stylesheet" href="https://fonts.googleapis.com/css2?family=Arvo:wght@400;700&display=swap">
<style>
  :root {
    --page-bg: #d9dadc;
    --card-bg: #2e2d2d;
    --orange: #f26522;
    --white: #ffffff;
    --soft-white: #ececec;
  }
  * { margin: 0; padding: 0; box-sizing: border-box; }
  html, body {
    width: 1200px;
    height: 676px;
    overflow: hidden;
    background: var(--page-bg);
  }
  .stage {
    width: 1200px;
    height: 676px;
    display: flex;
    align-items: center;
    justify-content: center;
  }
  .card {
    position: relative;
    width: 900px;
    height: 549px;
    background: var(--card-bg);
    font-family: "Arvo", Georgia, serif;
    color: var(--white);
    overflow: hidden;
  }
  .brand {
    position: absolute;
    left: 62px;
    top: 78px;
    right: 30px;
  }
  .brand-line {
    display: flex;
    align-items: flex-end;
    gap: 12px;
  }
  .brand-name {
    font-size: 38px;
    font-weight: 400;
    letter-spacing: 0.5px;
    text-transform: uppercase;
    white-space: nowrap;
    line-height: 1;
  }
  .brand-name .accent { color: var(--orange); }
  .brand-rule {
    flex: 1;
    height: 3px;
    background: var(--orange);
    margin-bottom: 4px;
  }
  .services {
    margin-top: 12px;
    font-size: 17px;
    color: var(--orange);
    letter-spacing: 0.3px;
    white-space: nowrap;
  }
  .contacts {
    position: absolute;
    left: 62px;
    top: 195px;
    list-style: none;
  }
  .contact-row {
    display: flex;
    align-items: center;
    height: 46px;
    font-size: 23px;
    color: var(--soft-white);
  }
  .contact-row .name { text-transform: uppercase; color: var(--white); }
  .contact-icon {
    width: 34px;
    height: 34px;
    margin-right: 22px;
    flex: none;
  }
  .licence-band {
    position: absolute;
    left: 0;
    right: 0;
    top: 392px;
    height: 64px;
    background: var(--orange);
    display: flex;
    align-items: center;
    padding-left: 62px;
  }
  .licence {
    font-size: 24px;
    color: var(--white);
  }
</style>
</head>
<body>
<main class="stage">
  <section class="card" aria-label="The Pipe Lantern business card, back">
    <header class="brand">
      <div class="brand-line">
        <h1 class="brand-name"><span class="accent">The</span> Pipe Lantern <span class="accent">Pty Ltd.</span></h1>
        <span class="brand-rule"></span>
      </div>
      <p class="services">Plumbing . Drainage . Gas Fitting . Roofing . Jet Blasting . CCTV .</p>
    </header>

    <ul class="contacts">
      <li class="contact-row">
        <svg class="contact-icon" viewBox="0 0 34 34" aria-hidden="true">
          <rect x="2" y="2" width="30" height="30" rx="5" fill="none" stroke="#f26522" stroke-width="3"/>
        </svg>
        <span class="name">Cal Yardley</span>
      </li>
      <li class="contact-row">
        <svg class="contact-icon" viewBox="0 0 34 34" aria-hidden="true">
          <rect x="2" y="8" width="30" height="20" rx="2" fill="#f26522"/>
          <polyline points="3,9 17,20 31,9" fill="none" stroke="#2e2d2d" stroke-width="2.5"/>
        </svg>
        <span class="email">thepipelantern@mailkestrel.com</span>
      </li>
      <li class="contact-row">
        <svg class="contact-icon" viewBox="0 0 34 34" aria-hidden="true">
          <path d="M9 4 L14 10 L11 14 C13 19 16 22 20 24 L24 21 L30 26 L26 31 C15 30 4 19 3 8 Z" fill="#f26522"/>
        </svg>
        <span class="phone">0418672913</span>
      </li>
    </ul>

    <div class="licence-band">
      <p class="licence">Licence# 583016K</p>
    </div>
  </section>
</main>
</body>
</html>
```